Business Card Design

Im looking for a business card that will market/promote myself as in independent/freelancer in the beauty industry. Im looking for something very modern, and clean looking. no specific colors just something that doesnt look cheesy, would like a very professional look

Industry/Entity Type

Business

Contact Information for Business Card

Corinne Balstrade, Hairstylist(Cut, color, blowdry, style, extensions, straightening treatments), makeup artist, red carpet, in-salon, editorial, tv, film, contact is 5307419863 cbglam@mailbrook.net, LA based

```html
<!DOCTYPE html>
<html lang="en">
<head>
<meta charset="utf-8">
<title>Corinne Balstrade — Business Cards</title>
<link rel="stylesheet" href="https://fonts.googleapis.com/css2?family=Quicksand:wght@300;400&display=swap">
<style>
  :root {
    --rose: #f06584;
    --rose-soft: #fbc2d0;
    --rose-light: #fde0e7;
    --ink: #1c1c1c;
    --paper: #ffffff;
    --backdrop: #eeeae6;
    --dots: #22245a;
    --tool: #2a2a2e;
  }
  * { box-sizing: border-box; margin: 0; padding: 0; }
  html, body {
    width: 1200px; height: 976px; overflow: hidden;
    background: var(--backdrop);
    font-family: "Quicksand", sans-serif;
    font-weight: 300;
  }
  h1, h2, p, li { font-weight: 300; }
  .sheet {
    position: relative; width: 1200px; height: 976px;
    display: flex; flex-direction: column; align-items: center; justify-content: center; gap: 44px;
  }
  .card {
    position: relative; width: 760px; height: 434px;
    background: var(--paper);
    overflow: hidden;
    box-shadow: 0 6px 18px rgba(0,0,0,.12);
  }
  .edge { position: absolute; left: 0; right: 0; height: 7px; background: var(--rose); }
  .edge--top { top: 0; }
  .edge--bottom { bottom: 0; }
  .band { position: absolute; left: 0; right: 0; background: var(--rose); }

  /* Front */
  .card--front .band { top: 122px; height: 216px; }
  .front-name {
    position: absolute; left: 44px; top: 58px;
    font-size: 58px; line-height: 1; color: var(--ink); letter-spacing: 1px;
    white-space: nowrap;
  }
  .front-name .first { color: var(--rose); }
  .front-title {
    position: absolute; right: 40px; top: 150px;
    font-size: 34px; line-height: 1; color: var(--rose-soft); letter-spacing: 2px;
    white-space: nowrap;
  }
  .card--front .scissors { left: 40px; top: 214px; }
  .card--front .cut-line { left: 150px; right: 40px; top: 239px; }

  /* Back */
  .card--back .band { top: 7px; height: 300px; }
  .back-name {
    position: absolute; left: 44px; top: 34px;
    font-size: 54px; line-height: 1; color: var(--paper); letter-spacing: 1px;
    white-space: nowrap;
  }
  .back-title {
    position: absolute; left: 46px; top: 104px;
    font-size: 30px; line-height: 1.2; color: var(--ink); letter-spacing: 1px;
    white-space: nowrap;
  }
  .contact {
    position: absolute; left: 46px; top: 152px;
    list-style: none; font-size: 23px; line-height: 30px; color: var(--rose-light);
    font-weight: 400; letter-spacing: 1px;
  }
  .contact li { font-weight: 400; }
  .services {
    position: absolute; left: 46px; top: 262px;
    font-size: 23px; color: var(--paper); letter-spacing: 2px; white-space: nowrap;
  }
  .card--back .scissors { left: 40px; top: 332px; }
  .card--back .cut-line { left: 150px; right: 40px; top: 357px; }

  .scissors { position: absolute; width: 96px; height: 52px; }
  .scissors circle, .scissors line { stroke: var(--tool); fill: none; }
  .scissors path { fill: var(--tool); }
  .cut-line {
    position: absolute; height: 3px;
    background-image: radial-gradient(circle, var(--dots) 1.4px, transparent 1.6px);
    background-size: 12px 3px; background-repeat: repeat-x;
  }
</style>
</head>
<body>
<main class="sheet">
  <section class="card card--front">
    <div class="edge edge--top"></div>
    <div class="band"></div>
    <h1 class="front-name"><span class="first">Corinne</span> Balstrade</h1>
    <p class="front-title">Hairstylist &amp; Makeup Artist</p>
    <svg class="scissors" viewBox="0 0 96 52" role="img" aria-label="Scissors icon">
      <circle cx="14" cy="12" r="9" stroke-width="5"/>
      <circle cx="14" cy="40" r="9" stroke-width="5"/>
      <path d="M21 16 L94 34 L90 38 L19 22 Z"/>
      <path d="M21 36 L94 18 L90 14 L19 30 Z"/>
    </svg>
    <div class="cut-line"></div>
  </section>

  <section class="card card--back">
    <div class="edge edge--top"></div>
    <div class="band"></div>
    <h2 class="back-name">Corinne Balstrade</h2>
    <p class="back-title">Hairstylist &amp; Makeup Artist</p>
    <ul class="contact">
      <li>based in L.A.</li>
      <li>tel: 5307419863</li>
      <li>email: cbglam@mailbrook.net</li>
    </ul>
    <p class="services">red carpet • in-salon • editorial • tv • film</p>
    <svg class="scissors" viewBox="0 0 96 52" role="img" aria-label="Scissors icon">
      <circle cx="14" cy="12" r="9" stroke-width="5"/>
      <circle cx="14" cy="40" r="9" stroke-width="5"/>
      <path d="M21 16 L94 34 L90 38 L19 22 Z"/>
      <path d="M21 36 L94 18 L90 14 L19 30 Z"/>
    </svg>
    <div class="cut-line"></div>
    <div class="edge edge--bottom"></div>
  </section>
</main>
</body>
</html>
```